Pemby Icewear Brochure

tagline_
- skatewear for everywhere

Brochure to showcase our clothing line/products
Sending to various stores around the country for them to carry the line.
Fun, attention getting brochure.
Template that we can change per season for different clothing/new products.
I've included my logo and can provide all photo's of current clothing that will need to be included in the brochure.

PLEASE USE IMAGE IMG_1454.JPG FOR COVER OF BROCHURE

Target Market(s)

Figure Skaters around the world. Age range anywhere between 4yrs old to an adult skater. Ice Skaters and fan's of ice skating. Female

Industry/Entity Type

Clothing

Requirements
Must have
• All photo's of clothing products/ descriptions

Must have product description next to each photo.
Velvet Comet etc.

Mission statement:
At Pemby our goal is to provide you cutting edge, super stylish, high quality apparel that’s wearable on the ice or out on the town.

Contact information for Brochure.

Contact us at:
Pemby Icewear
PO Box 4073
Sun Valley, Idaho 83353
Phone: 208-555-0148
Email: info@pembyicewear.example
www.pembyicewear.example
www.facebook.example/pembyicewear
www.twitter.example/pembyicewear

```html
<!DOCTYPE html>
<html lang="en">
<head>
<meta charset="utf-8">
<title>Pemby Icewear Brochure</title>
<link rel="stylesheet" href="https://fonts.googleapis.com/css2?family=Arimo&family=Rammetto+One&display=swap">
<style>
  :root {
    --paper: #ffffff;
    --ink: #111111;
    --band: #221c1b;
    --red: #d9261c;
    --blue: #0a8ad6;
    --orange: #e5761e;
    --magenta: #de137a;
    --yellow: #f7c20a;
    --green: #7cc02a;
    --fold: #9a9a9a;
  }
  html, body { margin: 0; padding: 0; overflow: hidden; background: var(--paper); }
  .canvas { position: relative; width: 1200px; height: 1000px; overflow: hidden; background: var(--paper); }
  .view-label {
    position: absolute; margin: 0;
    font-family: "Arimo", Arial, sans-serif; font-weight: 400;
    font-size: 27px; color: var(--ink);
  }
  .view-label--outside { left: 141px; top: 117px; }
  .view-label--inside { left: 915px; top: 108px; }
  .sheet {
    position: absolute; left: 0; top: 0;
    filter: drop-shadow(5px 6px 4px rgba(0,0,0,0.45));
  }
  .product {
    position: absolute; width: 190px; margin: 0;
    text-align: center; color: #fff;
    font-family: "Arimo", Arial, sans-serif; font-size: 10.5px; line-height: 13.5px;
    white-space: nowrap;
  }
  .product__name {
    display: block; margin-bottom: 3px;
    font-family: "Rammetto One", "Arial Black", sans-serif;
    font-size: 12px; line-height: 16px; font-weight: 400;
  }
  .product--rink-sweetheart { left: 182px; top: 240px; }
  .product--velvet-comet { left: 263px; top: 704px; }
  .product--crossbone-edge { left: 783px; top: 229px; }
  .product--frosted-hearts { left: 863px; top: 715px; }
</style>
</head>
<body>
<main class="canvas">
  <h2 class="view-label view-label--outside">front back</h2>
  <h2 class="view-label view-label--inside">inside</h2>

  <svg class="sheet" width="1200" height="1000" viewBox="0 0 1200 1000">
    <defs>
      <linearGradient id="photo-brunette" x1="0" y1="0" x2="1" y2="1">
        <stop offset="0" stop-color="#8c9a8a"/>
        <stop offset="0.35" stop-color="#b58e78"/>
        <stop offset="0.7" stop-color="#3a3236"/>
        <stop offset="1" stop-color="#9fb4c6"/>
      </linearGradient>
      <linearGradient id="photo-blonde-child" x1="0" y1="0" x2="0" y2="1">
        <stop offset="0" stop-color="#e9d3a4"/>
        <stop offset="0.4" stop-color="#f3e6d6"/>
        <stop offset="1" stop-color="#f7f4f3"/>
      </linearGradient>
      <linearGradient id="photo-ringer-tee" x1="0" y1="0" x2="0" y2="1">
        <stop offset="0" stop-color="#f1ede6"/>
        <stop offset="0.35" stop-color="#e8caa8"/>
        <stop offset="0.7" stop-color="#eeeaf0"/>
        <stop offset="1" stop-color="#4a3a30"/>
      </linearGradient>
      <linearGradient id="photo-black-tank" x1="0" y1="0" x2="1" y2="1">
        <stop offset="0" stop-color="#56677a"/>
        <stop offset="0.35" stop-color="#d4b58c"/>
        <stop offset="0.7" stop-color="#25202a"/>
        <stop offset="1" stop-color="#1b1820"/>
      </linearGradient>
    </defs>

    <g class="spread spread--outside">
      <rect role="img" aria-label="Photo of a smiling brunette skater in the black Velvet Comet tank" x="27" y="160" width="320" height="708" fill="url(#photo-brunette)"/>
      <polygon role="img" aria-label="Photo of a smiling blonde girl wearing the white Rink Sweetheart tee" points="190,160 562,160 562,868 400,868" fill="url(#photo-blonde-child)"/>
      <polygon class="stripe stripe--red" points="140,160 152,160 348,868 335,868" fill="var(--red)"/>
      <polygon class="band" points="152,160 252,160 452,868 348,868" fill="var(--band)"/>
      <polygon class="stripe stripe--blue" points="252,160 265,160 465,868 452,868" fill="var(--blue)"/>
      <line class="fold" x1="415.5" y1="160" x2="415.5" y2="868" stroke="var(--fold)" stroke-width="1"/>
      <rect class="back-panel" x="562" y="160" width="83" height="708" fill="var(--band)"/>

      <circle cx="277" cy="288" r="97" fill="var(--blue)"/>
      <circle cx="354" cy="206" r="36" fill="var(--orange)"/>
      <circle cx="392" cy="265" r="19" fill="var(--magenta)"/>
      <circle cx="358" cy="751" r="97" fill="var(--red)"/>
      <circle cx="274" cy="669" r="36" fill="var(--blue)"/>
      <circle cx="236" cy="728" r="19" fill="var(--yellow)"/>
    </g>

    <g class="spread spread--inside">
      <rect role="img" aria-label="Photo of a smiling blonde skater in the Frosted Hearts ringer tee" x="645" y="160" width="300" height="708" fill="url(#photo-ringer-tee)"/>
      <polygon role="img" aria-label="Photo of a smiling skater in the black Crossbone Edge tank" points="860,160 1178,160 1178,868 1060,868" fill="url(#photo-black-tank)"/>
      <polygon class="stripe stripe--magenta" points="742,160 755,160 948,868 935,868" fill="var(--magenta)"/>
      <polygon class="band" points="755,160 855,160 1060,868 948,868" fill="var(--band)"/>
      <polygon class="stripe stripe--green" points="855,160 868,160 1075,868 1060,868" fill="var(--green)"/>
      <line class="fold" x1="793.5" y1="160" x2="793.5" y2="868" stroke="var(--fold)" stroke-width="1"/>

      <circle cx="878" cy="270" r="96" fill="var(--green)"/>
      <circle cx="865" cy="358" r="37" fill="var(--blue)"/>
      <circle cx="928" cy="388" r="19" fill="var(--magenta)"/>
      <circle cx="958" cy="750" r="97" fill="var(--magenta)"/>
      <circle cx="881" cy="670" r="36" fill="var(--yellow)"/>
      <circle cx="843" cy="728" r="19" fill="var(--orange)"/>
    </g>
  </svg>

  <p class="product product--rink-sweetheart">
    <strong class="product__name">Rink Sweetheart</strong>
    White Tee<br>100% Cotton<br>Graphic:<br>“I like boys...I love figure skating”<br>Price: $22.00<br>Size: Adults and Kids
  </p>
  <p class="product product--velvet-comet">
    <strong class="product__name">Velvet Comet</strong>
    Black Tank<br>98% Cotton 2% Spandex<br>Graphic:<br>Be the queen<br>Price: $28.00<br>Size: Adults
  </p>
  <p class="product product--crossbone-edge">
    <strong class="product__name">Crossbone Edge</strong>
    Black Tank<br>100% Cotton<br>Price: $26.00<br>Size: Kids
  </p>
  <p class="product product--frosted-hearts">
    <strong class="product__name">Frosted Hearts</strong>
    Ringer Tee with Fuchsia<br>100% Cotton<br>Price: $22.00<br>Size: Adults and Kids
  </p>
</main>
</body>
</html>
```